Wash and Wear travel bag design

I want a design-proposal for a wash and wear travel bag. There is an example attached of the product but I want something much more classy. Maybe with prints on like the bra and panties but more simplistic. In one compartment you will have clean underwear when you travel and in the other one you put the ones for laundry. I will attach our logo as well and I would like to place it somewhere in the design but not sure where, maybe just as a tag/flap on the side. Please use your imagination and creativity. The wash and wear will come in black and beige so rather no other colors than these.

Target Market(s)

Women 18-35

Requirements
Should not have
• Too young design, not to messy! I want it simplistic!

```html
<!DOCTYPE html>
<html lang="en">
<head>
<meta charset="utf-8">
<title>Wash and Wear Travel Bag</title>
<link href="https://fonts.googleapis.com/css2?family=Arimo:wght@400;700&display=swap" rel="stylesheet">
<style>
  :root {
    --page: #ffffff;
    --bag-black: #000000;
    --bag-beige: #dccbae;
    --ink-light: #ffffff;
    --ink-dark: #000000;
    --tag-red: #ff0a14;
    --tag-ink: #e9e4dc;
  }
  html, body {
    margin: 0;
    padding: 0;
    width: 968px;
    height: 1200px;
    overflow: hidden;
    background: var(--page);
  }
  .canvas {
    position: relative;
    width: 968px;
    height: 1200px;
    font-family: "Arimo", Helvetica, Arial, sans-serif;
  }
  .bag {
    position: absolute;
    left: 84px;
    width: 795px;
    height: 447px;
  }
  .bag--black { top: 88px; background: var(--bag-black); color: var(--ink-light); }
  .bag--beige { top: 650px; background: var(--bag-beige); color: var(--ink-dark); }

  .compartment {
    position: absolute;
    top: 176px;
    width: 200px;
    margin-left: -100px;
    text-align: center;
  }
  .compartment--wear { left: 199px; }
  .compartment--wash { left: 596px; }

  .compartment__label {
    display: block;
    font-size: 40px;
    font-weight: 400;
    line-height: 1;
    letter-spacing: 0.5px;
    margin: 0 0 12px;
  }
  .compartment__icon {
    display: block;
    margin: 0 auto;
    fill: none;
    stroke: currentColor;
    stroke-width: 1.6;
    stroke-linejoin: round;
    stroke-linecap: round;
  }

  .brand-tag {
    position: absolute;
    left: 795px;
    top: 93px;
    width: 49px;
    height: 52px;
    background: var(--tag-red);
    display: flex;
    align-items: center;
    justify-content: center;
    gap: 3px;
    flex-direction: column;
  }
  .brand-tag__dot {
    width: 18px;
    height: 18px;
    border-radius: 50%;
    background: var(--tag-ink);
  }
  .brand-tag__name {
    font-size: 10px;
    font-weight: 700;
    letter-spacing: 0.5px;
    color: var(--tag-ink);
    line-height: 1;
  }
</style>
</head>
<body>
<main class="canvas">

  <section class="bag bag--black" aria-label="Black travel bag">
    <div class="compartment compartment--wear">
      <span class="compartment__label">WEAR</span>
      <svg class="compartment__icon" width="52" height="40" viewBox="0 0 52 40" aria-hidden="true">
        <path d="M5 2 C5 8 1 18 1 26 C1 34 8 38 16 37 C20 37 23 36 24 34 L24 30 L28 30 L28 34 C29 36 32 37 36 37 C44 38 51 34 51 26 C51 18 47 8 47 2"/>
        <path d="M5 10 L24 30 M47 10 L28 30"/>
        <rect x="24" y="29" width="4" height="6"/>
      </svg>
    </div>
    <div class="compartment compartment--wash">
      <span class="compartment__label">WASH</span>
      <svg class="compartment__icon" width="52" height="32" viewBox="0 0 52 32" aria-hidden="true">
        <path d="M1 3 C17 0 35 0 51 3 L50 7 C42 10 36 16 30 28 C28 31 24 31 22 28 C16 16 10 10 2 7 Z"/>
      </svg>
    </div>
    <div class="brand-tag" aria-label="LUNE">
      <span class="brand-tag__dot"></span>
      <span class="brand-tag__name">LUNE</span>
    </div>
  </section>

  <section class="bag bag--beige" aria-label="Beige travel bag">
    <div class="compartment compartment--wear">
      <span class="compartment__label">WEAR</span>
      <svg class="compartment__icon" width="52" height="40" viewBox="0 0 52 40" aria-hidden="true">
        <path d="M5 2 C5 8 1 18 1 26 C1 34 8 38 16 37 C20 37 23 36 24 34 L24 30 L28 30 L28 34 C29 36 32 37 36 37 C44 38 51 34 51 26 C51 18 47 8 47 2"/>
        <path d="M5 10 L24 30 M47 10 L28 30"/>
        <rect x="24" y="29" width="4" height="6"/>
      </svg>
    </div>
    <div class="compartment compartment--wash">
      <span class="compartment__label">WASH</span>
      <svg class="compartment__icon" width="52" height="32" viewBox="0 0 52 32" aria-hidden="true">
        <path d="M1 3 C17 0 35 0 51 3 L50 7 C42 10 36 16 30 28 C28 31 24 31 22 28 C16 16 10 10 2 7 Z"/>
      </svg>
    </div>
    <div class="brand-tag" aria-label="LUNE">
      <span class="brand-tag__dot"></span>
      <span class="brand-tag__name">LUNE</span>
    </div>
  </section>

</main>
</body>
</html>
```